Business Card Design for Bright Easel Designs

I need a business card design for Artist Marlon Teague who specializes in Digital Fine Art, Digital Illustration, Murals and Mixed Media. Digital art techniques combine the use of a computer and specialized programs coupled with the same methods and theories used to produce traditional art. The final design should use the new logo that was just deigned and reflect an artist who has embraced the evolution of art by using modern technology to paint vibrant, stunning and high quality art. Please make this a double sided card and use the attached photo on the back of the card. Please include the name of the business: Bright Easel Designs, Artist: Marlon Teague, Phone: 555-872-3096 Website: brighteaseldesigns.example

Target Market(s)

Anyone looking for fine art for there home or business.

Industry/Entity Type

Computer

Contact Information for Business Card

This should be a double sided business card with a modern feel to it.

Font styles to use
Sans Serif

Requirements
Must have
• Artist Name: Marlon Teague
• Business Name and Logo: Bright Easel Designs
• Phone: 555-872-3096
• Website: brighteaseldesigns.example
• specializes in Digital Fine Art, Digital Illustration, Murals and Mixed Media
Nice to have
• Black background with new logo that is attached to file

```html
<!DOCTYPE html>
<html lang="en">
<head>
<meta charset="utf-8">
<title>Bright Easel Designs – Business Card</title>
<link href="https://fonts.googleapis.com/css2?family=Exo+2:wght@400;500;600;700&display=swap" rel="stylesheet">
<style>
  :root {
    --backdrop: #e9e9ec;
    --card-white: #fbfbfc;
    --royal-blue: #0c1f9a;
    --accent-orange: #f7a21b;
    --name-grey: #3c3c44;
    --text-white: #ffffff;
  }
  html, body {
    margin: 0;
    width: 1200px;
    height: 901px;
    overflow: hidden;
    background: var(--backdrop);
    font-family: "Exo 2", sans-serif;
  }
  .card {
    position: absolute;
    left: 100px;
    top: 165px;
    width: 1000px;
    height: 572px;
    border-radius: 44px;
    overflow: hidden;
    background: var(--card-white);
    box-shadow: 0 10px 30px rgba(0,0,0,0.18);
  }
  .card-waves {
    position: absolute;
    inset: 0;
    width: 100%;
    height: 100%;
  }
  .brand {
    position: absolute;
    left: 150px;
    top: 120px;
    display: flex;
    align-items: center;
    gap: 14px;
  }
  .brand-dot {
    width: 34px;
    height: 34px;
    border-radius: 50%;
    background: var(--accent-orange);
  }
  .brand-name {
    font-size: 34px;
    font-weight: 700;
    color: var(--royal-blue);
    letter-spacing: 0.5px;
  }
  .person {
    position: absolute;
    left: 175px;
    top: 270px;
  }
  .person-name {
    font-size: 25px;
    font-weight: 500;
    letter-spacing: 1.5px;
    color: var(--name-grey);
    margin: 0;
  }
  .person-title {
    font-size: 18px;
    font-weight: 500;
    color: var(--royal-blue);
    margin: 4px 0 0 26px;
  }
  .contact {
    position: absolute;
    right: 40px;
    top: 318px;
    text-align: right;
    color: var(--text-white);
    font-size: 20px;
    font-weight: 500;
    letter-spacing: 0.6px;
  }
  .contact-address {
    margin: 0 0 16px;
    line-height: 1.3;
  }
  .contact-line {
    display: flex;
    justify-content: flex-end;
    align-items: center;
    gap: 12px;
    height: 32px;
  }
  .contact-line.small { font-size: 17px; height: 28px; }
  .contact-icon {
    width: 18px;
    height: 18px;
    flex: none;
  }
</style>
</head>
<body>
  <div class="card">
    <svg class="card-waves" viewBox="0 0 1000 572" preserveAspectRatio="none" aria-hidden="true">
      <path d="M0,250 C130,370 300,440 480,452 C310,452 140,410 0,330 Z" fill="var(--accent-orange)"/>
      <path d="M0,318 C160,420 330,465 500,452 C590,440 700,250 1000,170 L1000,572 L0,572 Z" fill="var(--royal-blue)"/>
      <path d="M560,436 C630,415 680,215 1000,132" fill="none" stroke="var(--royal-blue)" stroke-width="8"/>
    </svg>

    <div class="brand">
      <span class="brand-dot"></span>
      <span class="brand-name">Bright Easel Designs</span>
    </div>

    <div class="person">
      <p class="person-name">MARLON TEAGUE</p>
      <p class="person-title">Managing Director</p>
    </div>

    <div class="contact">
      <p class="contact-address">214 Canvas Row<br>Easton Hill</p>
      <div class="contact-line">555 872 3096
        <svg class="contact-icon" viewBox="0 0 24 24"><path d="M6.6 10.8a15 15 0 0 0 6.6 6.6l2.2-2.2a1 1 0 0 1 1-.25 11.4 11.4 0 0 0 3.6.6 1 1 0 0 1 1 1V20a1 1 0 0 1-1 1A17 17 0 0 1 3 4a1 1 0 0 1 1-1h3.5a1 1 0 0 1 1 1c0 1.25.2 2.45.6 3.6a1 1 0 0 1-.25 1z" fill="#fff"/></svg>
      </div>
      <div class="contact-line">555 872 3097
        <svg class="contact-icon" viewBox="0 0 24 24"><rect x="6" y="2" width="12" height="20" rx="2" fill="none" stroke="#fff" stroke-width="2"/><circle cx="12" cy="18" r="1.2" fill="#fff"/></svg>
      </div>
      <div class="contact-line">555 872 3098
        <svg class="contact-icon" viewBox="0 0 24 24"><rect x="4" y="8" width="16" height="13" rx="1.5" fill="#fff"/><rect x="7" y="3" width="10" height="6" fill="none" stroke="#fff" stroke-width="2"/></svg>
      </div>
      <div class="contact-line small">hello@brighteasel.example
        <svg class="contact-icon" viewBox="0 0 24 24"><rect x="3" y="5" width="18" height="14" rx="1.5" fill="#fff"/><path d="M3 6l9 7 9-7" fill="none" stroke="var(--royal-blue)" stroke-width="1.8"/></svg>
      </div>
      <div class="contact-line small">www.brighteaseldesigns.example
        <svg class="contact-icon" viewBox="0 0 24 24"><circle cx="12" cy="12" r="9.5" fill="none" stroke="#fff" stroke-width="2"/><ellipse cx="12" cy="12" rx="4" ry="9.5" fill="none" stroke="#fff" stroke-width="1.6"/><path d="M2.5 12h19M4.5 7h15M4.5 17h15" stroke="#fff" stroke-width="1.4"/></svg>
      </div>
    </div>
  </div>
</body>
</html>
```